Mexican Restaurant - Flyer for takeaway and delivery customers

We are a Mexican Restaurant.  We need a flyer for home delivery customers...should include our menu, photos, prices and location etc....
I have attached our menu, logo and some photos...feel free to use some of your own.  Please ask if you have any questions.
we prefer a one page (front and back) A4 or A5 size.  If that is not possible because of the number of items, maybe a booklet type flyer is acceptable.
WE also need the following text:
Salsa Verdal - New in KMBQ!
Unit R7-23
Level R7
Gable Heights
Kestrel Meridian Business Quarter
The phone number of :  04 318 5902
And the verbiage "Free Parking Available"!
Please reference the colors on the examples provided
If you can use Minion Pro font that would be great

```html
<!DOCTYPE html>
<html lang="en">
<head>
<meta charset="utf-8">
<title>Salsa Verdal – Flyer</title>
<link href="https://fonts.googleapis.com/css2?family=Crimson+Text:wght@400;600;700&display=swap" rel="stylesheet">
<style>
  :root{
    --red:#e8283a;
    --blue:#29b6e6;
    --ink:#231f20;
    --paper:#ffffff;
    --backdrop:#efece6;
  }
  *{box-sizing:border-box;margin:0;padding:0}
  html,body{width:1200px;height:909px;overflow:hidden;background:var(--backdrop)}
  body{position:relative;font-family:"Crimson Text",serif;color:var(--ink)}

  .page{position:absolute;top:124px;width:518px;height:733px;background:var(--red)}
  .page--front{left:54px}
  .page--back{left:628px}
  .page-pattern{position:absolute;inset:0;background:var(--red)}
  .panel{position:absolute;left:35px;top:35px;width:450px;height:663px;background:var(--paper);border:4px solid var(--blue)}

  /* front */
  .hero-photo{position:absolute;left:0;top:0;width:442px;height:250px;
    background:linear-gradient(135deg,#d9c9a8 0%,#c98a6a 35%,#3fa9c4 60%,#2a2a2a 100%)}
  .zigzag{position:absolute;left:0;top:232px;width:442px;height:20px}
  .brand-name{position:absolute;left:0;width:442px;top:286px;text-align:center;color:var(--red);font-size:70px;font-weight:400;line-height:1}
  .tagline{position:absolute;left:0;width:442px;top:372px;text-align:center;color:var(--blue);font-size:20px;letter-spacing:1.5px}
  .promo-box{position:absolute;top:430px;width:180px;height:81px;text-align:center;display:flex;flex-direction:column;justify-content:center;line-height:1.05}
  .promo-box--new{left:33px;border:2px solid var(--blue)}
  .promo-box--parking{left:236px;border:2px solid var(--red)}
  .promo-box .line-red{color:var(--red);font-size:25px;font-weight:600}
  .promo-box .line-blue{color:var(--blue);font-size:25px;font-weight:600}
  .pin{position:absolute;left:31px;top:547px;width:58px;height:78px}
  .address{position:absolute;left:99px;top:548px;font-size:14.5px;line-height:17px;font-style:normal}
  .call{position:absolute;left:236px;top:546px;width:180px;text-align:center}
  .call-label{color:var(--red);font-size:17px;font-weight:600;padding-bottom:3px;border-bottom:3px solid var(--red)}
  .call-number{color:var(--red);font-size:33px;font-weight:600;line-height:48px;border-bottom:3px solid var(--red)}

  /* back */
  .menu-tab{position:absolute;left:194px;top:0;width:130px;height:57px;background:var(--red);border:4px solid var(--blue);border-top:none;color:#fff;font-size:30px;font-weight:700;text-align:center;line-height:60px;letter-spacing:.5px}
  .menu-col{position:absolute;width:201px}
  .menu-col--left{left:14px}
  .menu-col--right{left:229px}
  .section-title{color:var(--red);font-size:15px;font-weight:600;line-height:18px;margin-bottom:2px}
  .item-name{color:var(--blue);font-size:10.5px;font-weight:600;line-height:12px}
  .row{display:flex;justify-content:space-between;align-items:flex-end;font-size:6.2px;line-height:12.4px}
  .row .price{font-size:8.5px;white-space:nowrap;padding-left:4px}
  .note{font-size:6.2px;line-height:8px}
  .food-photo{position:absolute}
  .photo-tacos{left:14px;top:243px;width:201px;height:49px;background:linear-gradient(90deg,#6b3a22,#c9a25b 40%,#d3352d 85%)}
  .photo-guac{left:229px;top:428px;width:202px;height:82px;background:linear-gradient(90deg,#5d6b2a,#d8b24a 45%,#3a3a2a 100%)}
  .photo-burrito{left:122px;top:480px;width:93px;height:62px;border-radius:40% 10% 40% 10%;background:linear-gradient(135deg,#f1e3c6,#c9785a 55%,#e9d7b4)}
  .burrito-title{position:absolute;left:14px;top:548px;color:var(--red);font-size:14.5px;font-weight:600;line-height:13px;width:201px}
  .burrito-details{position:absolute;left:14px;top:580px;width:201px}
</style>
</head>
<body>

<section class="page page--front">
  <div class="page-pattern" role="img" aria-label="Red background with white outline pattern of tacos and avocados"></div>
  <div class="panel">
    <div class="hero-photo" role="img" aria-label="Photo of rolled flour tortillas with filling and dipping sauces"></div>
    <svg class="zigzag" viewBox="0 0 442 20" preserveAspectRatio="none" aria-hidden="true">
      <polygon points="0,8 9,16 18,8 27,16 36,8 45,16 54,8 63,16 72,8 81,16 90,8 99,16 108,8 117,16 126,8 135,16 144,8 153,16 162,8 171,16 180,8 189,16 198,8 207,16 216,8 225,16 234,8 243,16 252,8 261,16 270,8 279,16 288,8 297,16 306,8 315,16 324,8 333,16 342,8 351,16 360,8 369,16 378,8 387,16 396,8 405,16 414,8 423,16 432,8 442,16 442,20 0,20" fill="#ffffff"/>
      <polyline points="0,8 9,16 18,8 27,16 36,8 45,16 54,8 63,16 72,8 81,16 90,8 99,16 108,8 117,16 126,8 135,16 144,8 153,16 162,8 171,16 180,8 189,16 198,8 207,16 216,8 225,16 234,8 243,16 252,8 261,16 270,8 279,16 288,8 297,16 306,8 315,16 324,8 333,16 342,8 351,16 360,8 369,16 378,8 387,16 396,8 405,16 414,8 423,16 432,8 442,16" fill="none" stroke="#29b6e6" stroke-width="3"/>
    </svg>
    <h1 class="brand-name">Salsa Verdal</h1>
    <p class="tagline">AUTHENTIC MEXICAN FOOD</p>
    <div class="promo-box promo-box--new">
      <span class="line-red">Salsa Verdal</span>
      <span class="line-blue">New in KMBQ!</span>
    </div>
    <div class="promo-box promo-box--parking">
      <span class="line-red">Free Parking</span>
      <span class="line-blue">Available</span>
    </div>
    <svg class="pin" viewBox="0 0 58 78" aria-hidden="true">
      <path d="M29 75 L8 44 A25 25 0 1 1 50 44 Z" fill="none" stroke="#29b6e6" stroke-width="3" stroke-linejoin="round"/>
      <circle cx="29" cy="28" r="12" fill="none" stroke="#29b6e6" stroke-width="3"/>
    </svg>
    <address class="address">
      Unit R7-23<br>Level R7<br>Gable Heights<br>Kestrel Meridian<br>Business Quarter
    </address>
    <div class="call">
      <div class="call-label">CALL US</div>
      <div class="call-number">04 318 5902</div>
    </div>
  </div>
</section>

<section class="page page--back">
  <div class="page-pattern" role="img" aria-label="Red background with white outline pattern of tacos and avocados"></div>
  <div class="panel">
    <div class="menu-col menu-col--left" style="top:36px">
      <h2 class="section-title">APPETIZERS</h2>
      <div class="item-name">Guacamole</div>
      <div class="row"><span>Served with our home-made corn tortilla chips (250g)</span><span class="price">42.00</span></div>
      <div class="item-name">Salsa Verdal Nachos</div>
      <div class="row"><span>Traditional (No meat)</span><span class="price">32.00</span></div>
      <div class="note">with either pastor (marinated steak), steak or chicken</div>
      <div class="row"><span></span><span class="price">44.00</span></div>
      <div class="item-name">Empanaditas</div>
      <div class="row"><span>Stuffed with chicken</span><span class="price">17.00</span></div>
      <div class="row"><span>Cheese</span><span class="price">22.00</span></div>
      <div class="item-name">Tacos dorados</div>
      <div class="row"><span>Served with fresh lettuce, tomato, cream and cheese</span><span class="price">22.00</span></div>
      <div class="item-name">Quesadilla</div>
      <div class="row"><span>with melted cheese served with cream and a dab of guacamole</span><span class="price">20.00</span></div>
      <div class="row"><span>Mushrooms</span><span class="price">25.00</span></div>
      <div class="row"><span>Pastor (marinated steak), steak or chicken</span><span class="price">30.00</span></div>
    </div>
    <div class="food-photo photo-tacos" role="img" aria-label="Photo of a plate of tacos with lime"></div>

    <div class="menu-col menu-col--left" style="top:302px">
      <h2 class="section-title">FROM THE GRILL</h2>
      <div class="item-name">Sope</div>
      <div class="row"><span>Served with refried beans, lettuce, cream and velvety cheese</span><span class="price">27.00</span></div>
      <div class="item-name">Huarache</div>
      <div class="note">Slightly thicker corn tortilla served with refried beans, cheese, lettuce, avocado, green or red salsa and the meat of your choice:</div>
      <div class="row"><span>Pastor (marinated steak), steak or chicken</span><span class="price">39.00</span></div>
      <div class="item-name">Tinga quesadilla</div>
      <div class="note">Corn tortilla served with freshly seasoned pulled chicken that has been marinated in a fresh tomato base served with refried</div>
      <div class="row"><span>beans, cheese, onion, coriander, and fresh tomato.</span><span class="price">40.00</span></div>
      <div class="row"><span>With mushrooms</span><span class="price">44.00</span></div>
      <div class="row"><span>Add extra cheese</span><span class="price">47.00</span></div>
      <div class="item-name">Volcan</div>
      <div class="row"><span>Three crispy corn tortillas served with melted cheese and steak</span><span class="price">48.00</span></div>
    </div>
    <div class="food-photo photo-burrito" role="img" aria-label="Photo of a halved burrito"></div>
    <h2 class="burrito-title">MAKE YOUR<br>OWN BURRITO!</h2>
    <div class="burrito-details">
      <div class="note">Base includes:<br>lettuce, refried beans or black beans, cream and cheese.</div>
      <div class="row"><span>Normal Size</span><span class="price">16.00</span></div>
      <div class="note">Mega Size<span style="float:right;font-size:8.5px">21.00</span><br>Your choice of meat (150g)</div>
      <div class="row"><span>Pastor (marinated steak) steak or chicken</span><span class="price">+10.00</span></div>
    </div>

    <div class="menu-col menu-col--right" style="top:36px">
      <h2 class="section-title">TACOS</h2>
      <div class="item-name">Ketaco</div>
      <div class="note">A hard taco shell that is made with cheese! Filled with your</div>
      <div class="row"><span>favorite pastor (marinated steak), steak or chicken</span><span class="price">37.00</span></div>
      <div class="item-name">Gringa</div>
      <div class="note">Two flour tortillas with pastor (marinated steak) grilled in</div>
      <div class="row"><span>flavorful cheese, coriander, onion and pineapple!</span><span class="price">37.00</span></div>
      <div class="item-name">Tacos al pastor</div>
      <div class="note">Marinated steak<span style="float:right;font-size:8.5px">30.00</span><br>Corn tortilla (order of 3) Flour tortilla (order of 2)</div>
      <div class="row"><span>Add cheese</span><span class="price">+5.00</span></div>
      <div class="item-name">Mula terca</div>
      <div class="row"><span>Two flour tortillas with steak, beef bacon and melted cheese</span><span class="price">40.00</span></div>
      <div class="item-name">Hawaiana</div>
      <div class="note">Salsa Verdal's secret, chicken, turkey breast ham, pineapple,</div>
      <div class="row"><span>beef bacon and cheese all inside three flour tortillas</span><span class="price">40.00</span></div>
      <div class="note">Chicken or steak<span style="float:right;font-size:8.5px">30.00</span><br>Corn tortilla (order of 3) Flour tortilla (order of 2)</div>
      <div class="row"><span>Cheese tortilla (order of 1) Add cheese</span><span class="price">+5.00</span></div>
      <div class="note">Veggie<span style="float:right;font-size:8.5px">30.00</span><br>Corn tortilla (order of 3) Flour tortilla (order of 2)</div>
      <div class="row"><span>Add cheese</span><span class="price">+5.00</span></div>
    </div>

    <div class="menu-col menu-col--right" style="top:302px">
      <h2 class="section-title">ALAMBRES</h2>
      <div class="item-name">Alambre tradicional</div>
      <div class="note">Beef bacon, bell peppers, onion, melted cheese with your choice of meat:</div>
      <div class="row"><span>Pastor (marinated steak), steak or chicken</span><span class="price">50.00</span></div>
      <div class="item-name">Alambre de barrio</div>
      <div class="note">All of your favorites from the Alambre tradicional but with</div>
      <div class="row"><span>a mix of pastor (marinated steak) and steak.</span><span class="price">55.00</span></div>
      <div class="item-name">Vegetarian alambre</div>
      <div class="row"><span>Onion, bell peppers, mushrooms and cheese</span><span class="price">47.00</span></div>
    </div>
    <div class="food-photo photo-guac" role="img" aria-label="Photo of guacamole with tortilla chips and avocado"></div>

    <div class="menu-col menu-col--right" style="top:523px">
      <h2 class="section-title">DESERTS</h2>
      <div class="item-name">Arroz con leche</div>
      <div class="note">Mexico's rice pudding, with a touch of cinnamon for</div>
      <div class="row"><span>more delicious.</span><span class="price">10.00</span></div>
      <div class="item-name">Flan</div>
      <div class="row"><span>Custard base dessert with a flavorful caramel on top</span><span class="price">10.00</span></div>
      <div class="item-name">Fruit chamoy</div>
      <div class="note">All areas of your taste buds will be affected by this truly Mexican's savory sauce. A salty, sweet, sour and a mild</div>
      <div class="row"><span>spice sauce drizzled over fresh fruit.</span><span class="price">15.00</span></div>
    </div>
  </div>
  <div class="menu-tab">MENU</div>
</section>

</body>
</html>
```